Washing powder bag design.

Project Description – Graphic Design Proposal for ORNE Laundry Powder Packaging
We have already explored initial design ideas internally, supported by AI-assisted tools (ChatGPT) to develop early concepts, layouts, and mockups. To support this, we have attached the bag die-cut, where graphics and text are placed as a visual guideline for the intended structure. In addition, we have included a mockup of the product series currently under development to clearly communicate the desired style, direction, and overall visual identity.
The mockup should be regarded as the design foundation for this project and as a starting point for professional refinement.
Scope of Work
We would like you to create three graphic design variants, each based on a different color direction:
1. Variant 1: In line with our current color scheme
2. Variant 2: A blue version
3. Variant 3: A green version
Design Elements to Be Preserved
The following elements must be maintained across all three variants:
• The overall style and visual expression of the mockup
• The leaf-shaped element in the bottom right corner
• The ORNE layout, including typography, positioning, and general look & feel
Summary
While the color palette may vary, the structure, style, and key design elements must remain consistent and be directly based on the attached mockup.
We look forward to seeing your creative interpretation and professional input.
Updates
We need the design to be created based on the attached die-cut file “Orne 10 kg BAG 202526”, including all text elements.
We would like the final to include both the designed die-cut file and a mockup.

```html
<!DOCTYPE html>
<html lang="da">
<head>
<meta charset="utf-8">
<title>ORNE Vaskepulver – tre farvevarianter</title>
<link href="https://fonts.googleapis.com/css2?family=Open+Sans:wght@600;700;800&display=swap" rel="stylesheet">
<style>
  :root {
    --canvas: #ffffff;
    --cream-bag: #f1ece0;
    --cream-text: #5a7d69;
    --cream-dark: #1f4a37;
    --cream-circle: #d3dfc4;
    --cream-leaf: #b9cfa6;
    --green-bag: #dce9df;
    --green-text: #577a66;
    --green-dark: #1f4a37;
    --green-circle: #c3dbbe;
    --green-leaf: #a8c99c;
    --blue-bag: #dcecef;
    --blue-text: #5b6881;
    --blue-dark: #252f4f;
    --blue-circle: #bcd8dd;
    --blue-leaf: #a6c8cd;
    --seal-line: rgba(0,0,0,0.06);
    --hole-line: rgba(0,0,0,0.35);
  }
  * { box-sizing: border-box; margin: 0; padding: 0; }
  html, body { width: 1200px; height: 686px; overflow: hidden; background: var(--canvas); }
  body { position: relative; font-family: "Open Sans", Arial, sans-serif; }

  .bag {
    position: absolute; top: 98px; width: 264px; height: 516px;
    background: var(--bag); border-radius: 4px;
    color: var(--text);
  }
  .bag--cream { left: 110px; --bag: var(--cream-bag); --text: var(--cream-text); --dark: var(--cream-dark); --circle: var(--cream-circle); --leaf: var(--cream-leaf); }
  .bag--green { left: 468px; --bag: var(--green-bag); --text: var(--green-text); --dark: var(--green-dark); --circle: var(--green-circle); --leaf: var(--green-leaf); }
  .bag--blue  { left: 826px; --bag: var(--blue-bag); --text: var(--blue-text); --dark: var(--blue-dark); --circle: var(--blue-circle); --leaf: var(--blue-leaf); }

  .seal { position: absolute; left: 0; right: 0; height: 12px; background: var(--seal-line); }
  .seal--top { top: 0; }
  .seal--band { top: 108px; }

  .hang-holes { position: absolute; top: 41px; left: 0; right: 0; display: flex; justify-content: center; gap: 8px; }
  .hang-hole { width: 36px; height: 36px; border: 1px solid var(--hole-line); border-radius: 50%; }

  .brand-mark {
    position: absolute; top: 140px; left: 64px; width: 136px; height: 136px;
    border-radius: 50%; background: var(--circle);
    display: flex; align-items: center; justify-content: center;
  }
  .brand-name { font-weight: 700; font-size: 48px; letter-spacing: 0.5px; color: var(--text); line-height: 1; }

  .line { position: absolute; left: 0; right: 0; text-align: center; line-height: 1; font-weight: 700; }
  .product-name { top: 284px; font-size: 28px; }
  .product-name-en { top: 314px; font-size: 15px; font-weight: 600; }
  .tagline { top: 345px; font-size: 15px; }
  .tagline + .tagline { top: 364px; }

  .usage { position: absolute; top: 405px; left: 40px; display: flex; align-items: center; gap: 8px; }
  .usage-icon {
    width: 33px; height: 33px; border-radius: 7px; background: var(--dark);
    display: flex; align-items: center; justify-content: center; color: #fff;
  }
  .usage-icon svg { width: 24px; height: 24px; }
  .dose { font-size: 11px; font-weight: 700; border: 1.5px solid #fff; border-radius: 4px; padding: 2px 2px; line-height: 1; }
  .weight { font-size: 14px; font-weight: 700; color: var(--dark); margin-left: 1px; }

  .temperatures { position: absolute; top: 442px; left: 36px; font-size: 10px; font-weight: 700; color: var(--dark); white-space: nowrap; }

  .leaf-art {
    position: absolute; left: 185px; top: 345px; width: 70px; height: 136px;
    border-radius: 50% 50% 45% 45%;
    background: radial-gradient(ellipse at 50% 45%, var(--leaf) 0%, transparent 72%);
    opacity: 0.85;
  }
</style>
</head>
<body>
  <main class="range">
    <section class="bag bag--cream">
      <div class="seal seal--top"></div>
      <div class="seal seal--band"></div>
      <div class="hang-holes"><span class="hang-hole"></span><span class="hang-hole"></span><span class="hang-hole"></span></div>
      <div class="brand-mark"><span class="brand-name">ORNE</span></div>
      <h2 class="line product-name">VASKEPULVER</h2>
      <p class="line product-name-en">LAUNDRY DETERGENT</p>
      <p class="line tagline">LIV OG BALANCE</p>
      <p class="line tagline">I HVERDAGEN</p>
      <div class="leaf-art" role="img" aria-label="Decorative leaf sprig illustration"></div>
      <div class="usage">
        <span class="usage-icon"><span class="dose">120</span></span>
        <span class="usage-icon"><svg viewBox="0 0 24 24" fill="none" stroke="currentColor" stroke-width="1.6"><rect x="4" y="3" width="16" height="18" rx="2"/><line x1="4" y1="7" x2="20" y2="7"/><circle cx="12" cy="14" r="4.2"/></svg></span>
        <span class="usage-icon"><svg viewBox="0 0 24 24" fill="none" stroke="currentColor" stroke-width="1.6"><path d="M3 12h18l-2 7H5z"/><path d="M9 12l2-6 3 1-1 5"/></svg></span>
        <span class="weight">10 Kg</span>
      </div>
      <p class="temperatures">20°C | 30°C | 40°C | 60°C | 90°C</p>
    </section>

    <section class="bag bag--green">
      <div class="seal seal--top"></div>
      <div class="seal seal--band"></div>
      <div class="hang-holes"><span class="hang-hole"></span><span class="hang-hole"></span><span class="hang-hole"></span></div>
      <div class="brand-mark"><span class="brand-name">ORNE</span></div>
      <h2 class="line product-name">VASKEPULVER</h2>
      <p class="line product-name-en">LAUNDRY DETERGENT</p>
      <p class="line tagline">LIV OG BALANCE</p>
      <p class="line tagline">I HVERDAGEN</p>
      <div class="leaf-art" role="img" aria-label="Decorative leaf sprig illustration"></div>
      <div class="usage">
        <span class="usage-icon"><span class="dose">120</span></span>
        <span class="usage-icon"><svg viewBox="0 0 24 24" fill="none" stroke="currentColor" stroke-width="1.6"><rect x="4" y="3" width="16" height="18" rx="2"/><line x1="4" y1="7" x2="20" y2="7"/><circle cx="12" cy="14" r="4.2"/></svg></span>
        <span class="usage-icon"><svg viewBox="0 0 24 24" fill="none" stroke="currentColor" stroke-width="1.6"><path d="M3 12h18l-2 7H5z"/><path d="M9 12l2-6 3 1-1 5"/></svg></span>
        <span class="weight">10 Kg</span>
      </div>
      <p class="temperatures">20°C | 30°C | 40°C | 60°C | 90°C</p>
    </section>

    <section class="bag bag--blue">
      <div class="seal seal--top"></div>
      <div class="seal seal--band"></div>
      <div class="hang-holes"><span class="hang-hole"></span><span class="hang-hole"></span><span class="hang-hole"></span></div>
      <div class="brand-mark"><span class="brand-name">ORNE</span></div>
      <h2 class="line product-name">VASKEPULVER</h2>
      <p class="line product-name-en">LAUNDRY DETERGENT</p>
      <p class="line tagline">LIV OG BALANCE</p>
      <p class="line tagline">I HVERDAGEN</p>
      <div class="leaf-art" role="img" aria-label="Decorative leaf sprig illustration"></div>
      <div class="usage">
        <span class="usage-icon"><span class="dose">120</span></span>
        <span class="usage-icon"><svg viewBox="0 0 24 24" fill="none" stroke="currentColor" stroke-width="1.6"><rect x="4" y="3" width="16" height="18" rx="2"/><line x1="4" y1="7" x2="20" y2="7"/><circle cx="12" cy="14" r="4.2"/></svg></span>
        <span class="usage-icon"><svg viewBox="0 0 24 24" fill="none" stroke="currentColor" stroke-width="1.6"><path d="M3 12h18l-2 7H5z"/><path d="M9 12l2-6 3 1-1 5"/></svg></span>
        <span class="weight">10 Kg</span>
      </div>
      <p class="temperatures">20°C | 30°C | 40°C | 60°C | 90°C</p>
    </section>
  </main>
</body>
</html>
```